Rancho Verbena Wine Bottle Label

Hello! We are looking for a wine bottle label design for our private, family winery located in Chico, CA. The name of our home/ranch/vineyard is Rancho Verbena ('the exit'), which is inspired by our hilltop location, panoramic views of the valley, and sensation of escaping from the busy world below.

We planted our vineyard in 2011 and are now bottling our first harvest from fall of 2013. We planted all Italian varietals on our land: syrah, primitivo, and montepulciano. The wine we make is the culmination of all the love, support and effort poured into the process by our family and friends.

The task at hand: we are looking for a clean, simple front and back wine label design.

Front Label Content:
RV and/or Rancho Verbena
Estate Grown
Chico, CA
Varietal (use Syrah for placeholder)
Year (use 2013 for placeholder)

Back Label Content:
Running list of names of all family and friends who have participated in the process (use a text fill for placeholder)

Aesthetic Description:
Simple, clean, contemporary, text based design (see attached logo idea, Image #1)
Like the brown paper with stamped lettering look & feel
Like the classic clear label with gold lettering look & feel
Option to incorporated a simple background image/sketch of the view overlooking the valley (see attached Image #2 and #3)
Additional inspirational images attached for reference (Images #3- )

General Size Requirement:
Front Label - 4"tall by 3 1/2" wide
Back Label - 4"tall by 3 1/2" wide

Format:
Please submit Photoshop or Illustrator or InDesign Files and PDF/EPS Files.

```html
<!DOCTYPE html>
<html lang="en">
<head>
<meta charset="utf-8">
<title>Rancho Verbena Syrah 2013 Label</title>
<link href="https://fonts.googleapis.com/css2?family=Questrial&family=Russo+One&display=swap" rel="stylesheet">
<style>
  :root {
    --page: #ffffff;
    --frame: #0d0d0d;
    --frame-line: #3a3a3a;
    --gold: #d9a934;
    --gold-deep: #c8962a;
    --ink: #111111;
    --mono-ink: #2b2b2b;
  }
  * { margin: 0; padding: 0; box-sizing: border-box; }
  html, body {
    width: 1200px;
    height: 1050px;
    overflow: hidden;
    background: var(--page);
  }
  .label {
    position: absolute;
    left: 53px;
    top: 53px;
    width: 1094px;
    height: 948px;
    background: var(--frame);
    border-radius: 8px;
  }
  .label__inner-rule {
    position: absolute;
    inset: 14px 16px;
    border: 2px solid var(--frame-line);
    border-radius: 4px;
  }
  .label__field {
    position: absolute;
    left: 36px;
    top: 28px;
    right: 36px;
    bottom: 28px;
    background: radial-gradient(ellipse at center, var(--gold) 55%, var(--gold-deep) 100%);
  }
  .monogram {
    position: absolute;
    left: 0;
    right: 0;
    top: 120px;
    text-align: center;
    font-family: "Questrial", sans-serif;
    font-size: 430px;
    line-height: 1;
    letter-spacing: -20px;
    color: var(--mono-ink);
  }
  .vintage {
    position: absolute;
    left: 0;
    right: 0;
    top: 595px;
    text-align: center;
    font-family: "Russo One", sans-serif;
    font-size: 58px;
    letter-spacing: 6px;
    color: var(--ink);
  }
  .varietal {
    position: absolute;
    left: 0;
    right: 0;
    top: 670px;
    text-align: center;
    font-family: "Russo One", sans-serif;
    font-size: 58px;
    letter-spacing: 5px;
    color: var(--ink);
  }
  .estate {
    position: absolute;
    left: 0;
    right: 0;
    top: 756px;
    text-align: center;
    font-family: "Questrial", sans-serif;
    font-size: 34px;
    color: var(--ink);
  }
</style>
</head>
<body>
  <div class="label">
    <div class="label__inner-rule"></div>
    <div class="label__field">
      <div class="monogram">RV</div>
      <div class="vintage">2013</div>
      <div class="varietal">SYRAH</div>
      <div class="estate">Rancho Verbena Estate GrownChico</div>
    </div>
  </div>
</body>
</html>
```